Sports Event Company designing web home page

Design a home page for a Sports event company. Our company is launching an innovative new sports event (quite similiar to adult tag rugby) and we need a slick , kool , innovative website to help us launch our event . Our website needs to portray us as an energetic sports company but yet give a level of professionalism and reassurance despite our product been new.

We have built a Registration system but have encountered that the better website developers are not necessarilt the best designers.

Target Market(s)

20 to 35 year olds who are sporty . Sports and social commitees from corporates

Industry/Entity Type

Adult

Requirements
Must have
• Strong ability to interact with social media

Easy to register for events

Bright but classy

Colour scheme transferrable to Flyers , posters etc

```html
<!DOCTYPE html>
<html lang="en">
<head>
<meta charset="utf-8">
<title>Tag Rush – Home</title>
<link href="https://fonts.googleapis.com/css2?family=Open+Sans:ital,wght@0,400;0,600;0,700;1,700&family=Cabin:wght@500;600&display=swap" rel="stylesheet">
<style>
:root{
  --red:#c8201c;
  --red-deep:#8c0d0d;
  --red-dark:#6e0808;
  --orange:#f4a23a;
  --ink:#333333;
  --grey-text:#4a4a4a;
  --page:#e9e9e9;
  --panel-top:#c9c9c9;
  --panel-bottom:#dedede;
  --white:#ffffff;
  --link:#c8201c;
  --foot:#c43a34;
  --foot-dark:#8a1010;
  --foot-link:#f3906c;
}
*{margin:0;padding:0;box-sizing:border-box}
a{text-decoration:none}
html,body{width:853px;height:1200px;overflow:hidden}
body{position:relative;background:var(--page);font-family:"Open Sans",Arial,sans-serif;color:var(--ink)}
.abs{position:absolute}

/* header */
.site-header{left:0;top:0;width:853px;height:52px;
  background:linear-gradient(180deg,#e8402a 0%,var(--red) 45%,#a8110f 100%)}
.brand{left:80px;top:12px;font-weight:600;font-size:24px;color:var(--white)}
.nav a{position:absolute;top:21px;font-size:10.5px;font-weight:600;color:var(--white);letter-spacing:.3px}
.nav .current{left:295px;top:17px;width:56px;height:21px;border:1px solid #f4b090;border-radius:3px;
  background:linear-gradient(#f0562e,#c4201a);text-align:center;line-height:19px}
.top-band{left:0;top:52px;width:853px;height:190px;background:linear-gradient(180deg,#d6d1cf,#dcdada 70%,#e2e2e2)}

/* hero */
.hero-frame{left:72px;top:70px;width:706px;height:278px;border-radius:6px;
  background:linear-gradient(#f6f2f0,#e4dcd8);box-shadow:0 2px 6px rgba(0,0,0,.25)}
.hero{left:86px;top:86px;width:676px;height:245px;
  background:radial-gradient(ellipse at 50% 100%,#f4742a 0%,var(--red) 45%,#a7120f 100%)}
.photo{border:6px solid #ecd8cf;box-shadow:0 2px 5px rgba(0,0,0,.4);
  background:linear-gradient(180deg,#6d6e70 0%,#8c8f8c 45%,#5f8f3e 55%,#4d7a32 100%)}
.hero-tagline{left:86px;top:289px;width:616px;text-align:center;font-family:"Cabin",sans-serif;font-weight:500;font-size:19px;color:var(--white)}
.pill{border-radius:18px;background:linear-gradient(#3a3a3a,#050505);border:3px solid #b51714;
  color:var(--white);font-weight:700;text-align:center;box-shadow:0 0 0 2px #e8542e}
.learn-more{left:622px;top:291px;width:135px;height:34px;font-size:8px;line-height:28px}

/* welcome */
.welcome{left:57px;top:367px;width:732px;height:151px;border-radius:8px;border:1px solid #cfcfcf;
  background:linear-gradient(180deg,var(--panel-top) 0%,var(--panel-top) 49%,var(--panel-bottom) 50%,#e4e4e4 100%)}
.welcome h1{position:absolute;left:41px;top:16px;font-size:17px;font-weight:400;color:#353535;letter-spacing:.3px}
.welcome p{position:absolute;left:41px;top:61px;width:650px;font-size:13.9px;line-height:23px;text-align:justify;color:#333;letter-spacing:.2px}
.welcome .more{position:absolute;left:627px;top:122px;font-size:10px;color:var(--link)}

/* features */
.feature-icon{border-radius:6px}
.feature h2{position:absolute;font-size:13.5px;font-weight:600;color:#333}
.feature p{position:absolute;width:183px;font-size:9.2px;line-height:13.5px;text-align:justify;color:var(--grey-text)}
.feature .more{position:absolute;font-size:9px;font-weight:700;font-style:italic;color:var(--link)}

/* register */
.register{left:578px;top:544px;width:212px;height:268px;border-radius:6px;border:1px solid #cfcfcf;background:#f1f1f1}
.register-inner{left:586px;top:552px;width:196px;height:253px;border-radius:6px;
  background:radial-gradient(ellipse at 50% 95%,#f06028 0%,var(--red) 40%,var(--red-deep) 100%)}
.register-head{left:586px;top:552px;width:196px;height:28px;border-radius:6px 6px 0 0;border-top:2px solid var(--orange);
  background:linear-gradient(#e0452a,#b8140f);color:var(--white);text-align:center;font-size:12.5px;font-weight:600;line-height:26px;letter-spacing:.5px}
.reg-label{font-size:9px;font-weight:600;color:var(--white);left:608px}
.reg-input{left:605px;width:154px;height:21px;border-radius:3px;background:linear-gradient(#e8b8b8,#f4d8d8)}
.sign-in{left:605px;top:731px;width:155px;height:36px;font-size:10px;line-height:30px}

/* games */
.rule{left:70px;width:710px;height:1px;background:#d2d2d2}
.games-title{left:73px;top:829px;font-size:13.5px;font-weight:600;color:#333}
.thumb{border:4px solid var(--white);box-shadow:0 1px 4px rgba(0,0,0,.35);
  background:linear-gradient(180deg,#5c5f66 0%,#7a7c80 40%,#5b8f3c 52%,#3f6e2a 100%)}
.play{position:absolute;left:50%;top:32%;width:36px;height:36px;margin-left:-18px}
.see-all{left:713px;top:969px;font-size:9px;color:var(--link)}

/* footer */
.footer{left:0;top:1003px;width:853px;height:145px;
  background:radial-gradient(ellipse at 33% 0%,#e87a6e 0%,var(--foot) 35%,#b8302a 100%)}
.footer h3{position:absolute;top:18px;font-size:9.5px;font-weight:700;color:var(--white);letter-spacing:.2px}
.footer p{position:absolute;width:180px;font-size:7.6px;line-height:10.5px;color:#ffe6e0}
.social{position:absolute;top:44px;width:15px;height:15px;border-radius:2px;background:#3f8fd0;box-shadow:0 1px 1px rgba(0,0,0,.3)}
.contact{font-size:8.5px!important;width:140px!important;color:var(--white)!important;line-height:14px!important}
.bottom-bar{left:0;top:1148px;width:853px;height:52px;background:var(--foot-dark)}
.bottom-bar a,.bottom-bar span{position:absolute;top:23px;font-size:7.5px;color:var(--foot-link)}
</style>
</head>
<body>

<header>
  <div class="abs site-header"></div>
  <div class="abs brand">Tag Rush</div>
  <nav class="nav">
    <a class="current" href="#">HOME</a>
    <a style="left:370px" href="#">ABOUT US</a>
    <a style="left:458px" href="#">SERVICES</a>
    <a style="left:541px" href="#">SCHEDULES</a>
    <a style="left:632px" href="#">BLOG</a>
    <a style="left:696px" href="#">CONTACT US</a>
  </nav>
</header>

<div class="abs top-band"></div>

<section>
  <div class="abs hero-frame"></div>
  <div class="abs hero"></div>
  <div class="abs photo" style="left:107px;top:127px;width:188px;height:132px" role="img" aria-label="Players in orange bibs chasing the ball on a grass pitch"></div>
  <div class="abs photo" style="left:563px;top:133px;width:153px;height:140px" role="img" aria-label="Two teams contesting a tag on the pitch near the clubhouse"></div>
  <div class="abs photo" style="left:291px;top:101px;width:275px;height:183px" role="img" aria-label="Mixed team match in front of the stand"></div>
  <div class="abs hero-tagline">The best place for&nbsp; Favorite Sports</div>
  <a class="abs pill learn-more" href="#">LEARN MORE</a>
</section>

<section class="abs welcome">
  <h1>WELCOME TO TAG RUSH</h1>
  <p>Lorem ipsum dolor sit amet, consectetur adipiscing elit. Curabitur eu interdum dui. Aliquam turpis mauris, rhoncus et tempus ac, pellentesque quis sem. Nullam a leo arcu, in posuere leo.</p>
  <a class="more" href="#">Read more...</a>
</section>

<section class="feature">
  <div class="abs feature-icon" style="left:55px;top:544px;width:43px;height:45px;background:linear-gradient(#6a9ad0,#2d5d96)" role="img" aria-label="Calendar icon"></div>
  <h2 style="left:102px;top:556px">Events</h2>
  <p style="left:102px;top:573px">adipiscing elit. Curabitur eu interdum dui. Aliquam turpis mauris, rhoncus et tempus ac, pellentesque quis sem. Nullam a leo arcu, in posuere leo.</p>
  <a class="more" style="left:227px;top:628px" href="#">Read more...</a>

  <div class="abs feature-icon" style="left:313px;top:544px;width:47px;height:46px;background:linear-gradient(#a8d4ee,#4a8fc4)" role="img" aria-label="Video clapper icon"></div>
  <h2 style="left:366px;top:556px">Videos</h2>
  <p style="left:366px;top:573px;width:186px">adipiscing elit. Curabitur eu interdum dui. Aliquam turpis mauris, rhoncus et tempus ac, pellentesque quis sem. Nullam a leo arcu, in posuere leo.</p>
  <a class="more" style="left:497px;top:628px" href="#">Read more...</a>

  <div class="abs feature-icon" style="left:57px;top:688px;width:47px;height:47px;background:linear-gradient(#4a8fd8,#1d5aa8)" role="img" aria-label="Newspaper icon"></div>
  <h2 style="left:110px;top:695px">News</h2>
  <p style="left:110px;top:712px;width:176px">adipiscing elit. Curabitur eu interdum dui. Aliquam turpis mauris, rhoncus et tempus ac, pellentesque quis sem. Nullam a leo arcu, in posuere leo.</p>
  <a class="more" style="left:226px;top:770px" href="#">Read more...</a>

  <div class="abs feature-icon" style="left:308px;top:688px;width:48px;height:48px;background:linear-gradient(#e8383a,#b01416)" role="img" aria-label="Speech bubbles icon"></div>
  <h2 style="left:370px;top:697px">Blog</h2>
  <p style="left:370px;top:714px;width:182px">adipiscing elit. Curabitur eu interdum dui. Aliquam turpis mauris, rhoncus et tempus ac, pellentesque quis sem. Nullam a leo arcu, in posuere leo.</p>
  <a class="more" style="left:495px;top:773px" href="#">Read more...</a>
</section>

<form>
  <div class="abs register"></div>
  <div class="abs register-inner"></div>
  <div class="abs register-head">REGISTER</div>
  <label class="abs reg-label" style="top:596px">Your Name</label>
  <div class="abs reg-input" style="top:613px"></div>
  <label class="abs reg-label" style="top:639px">Your Password</label>
  <div class="abs reg-input" style="top:654px"></div>
  <label class="abs reg-label" style="top:682px">Your Email</label>
  <div class="abs reg-input" style="top:694px"></div>
  <div class="abs pill sign-in">SIGN IN</div>
</form>

<section>
  <div class="abs rule" style="top:812px"></div>
  <h2 class="abs games-title">Latest Games</h2>
  <svg class="abs" style="left:50px;top:908px" width="12" height="16" viewBox="0 0 12 16"><path d="M9 2 3 8l6 6" fill="none" stroke="#8a8a8a" stroke-width="2.5"/></svg>
  <svg class="abs" style="left:788px;top:908px" width="12" height="16" viewBox="0 0 12 16"><path d="M3 2l6 6-6 6" fill="none" stroke="#8a8a8a" stroke-width="2.5"/></svg>

  <div class="abs thumb" style="left:73px;top:855px;width:161px;height:107px" role="img" aria-label="Match video: team running with the ball">
    <svg class="play" viewBox="0 0 36 36"><circle cx="18" cy="18" r="16" fill="rgba(40,40,40,.45)" stroke="rgba(255,255,255,.6)" stroke-width="2"/><path d="M14 11v14l11-7z" fill="rgba(255,255,255,.75)"/></svg>
  </div>
  <div class="abs thumb" style="left:249px;top:855px;width:161px;height:107px" role="img" aria-label="Match video: close tackle at midfield">
    <svg class="play" viewBox="0 0 36 36"><circle cx="18" cy="18" r="16" fill="rgba(40,40,40,.45)" stroke="rgba(255,255,255,.6)" stroke-width="2"/><path d="M14 11v14l11-7z" fill="rgba(255,255,255,.75)"/></svg>
  </div>
  <div class="abs thumb" style="left:429px;top:855px;width:160px;height:107px" role="img" aria-label="Match video: players spread across the pitch">
    <svg class="play" viewBox="0 0 36 36"><circle cx="18" cy="18" r="16" fill="rgba(40,40,40,.45)" stroke="rgba(255,255,255,.6)" stroke-width="2"/><path d="M14 11v14l11-7z" fill="rgba(255,255,255,.75)"/></svg>
  </div>
  <div class="abs thumb" style="left:610px;top:852px;width:161px;height:107px" role="img" aria-label="Match video: tag near the clubhouse">
    <svg class="play" viewBox="0 0 36 36"><circle cx="18" cy="18" r="16" fill="rgba(40,40,40,.45)" stroke="rgba(255,255,255,.6)" stroke-width="2"/><path d="M14 11v14l11-7z" fill="rgba(255,255,255,.75)"/></svg>
  </div>
  <a class="abs see-all" href="#">See All Videos</a>
  <div class="abs rule" style="top:983px"></div>
</section>

<footer>
  <div class="abs footer">
    <h3 style="left:71px">BLOG UPDATES</h3>
    <p style="left:71px;top:38px">Lorem ipsum dolor sit amet, consectetur adipiscing elit.</p>
    <p style="left:71px;top:66px">Cras sit amet urna quam. Lorem ipsum dolor sit amet</p>
    <p style="left:71px;top:94px">consectetur adipiscing elit. Cras sit amet urna quam</p>

    <h3 style="left:287px">LATEST NEWS</h3>
    <p style="left:287px;top:38px">Lorem ipsum dolor sit amet, consectetur adipiscing elit.</p>
    <p style="left:287px;top:66px">Cras sit amet urna quam. Lorem ipsum dolor sit amet</p>
    <p style="left:287px;top:94px">consectetur adipiscing elit. Cras sit amet urna quam</p>

    <h3 style="left:491px">OUR SOCIAL NETWORK</h3>
    <span class="social" style="left:502px"></span>
    <span class="social" style="left:523px"></span>
    <span class="social" style="left:544px"></span>
    <span class="social" style="left:565px"></span>
    <span class="social" style="left:586px;background:#c8c8c8"></span>

    <h3 style="left:655px">OUR CONTACT</h3>
    <p class="contact" style="left:649px;top:41px">Email: info@tagrush.com<br>Telephone: 000-000-0000</p>
  </div>
  <div class="abs bottom-bar">
    <a style="left:71px" href="#">home</a>
    <a style="left:117px" href="#">about us</a>
    <a style="left:175px" href="#">services</a>
    <a style="left:230px" href="#">Schedules</a>
    <a style="left:285px" href="#">blog</a>
    <a style="left:326px" href="#">contact us</a>
    <span style="left:561px">Copyright© 2012.&nbsp;&nbsp; www.tagrush.com. all rights reserved</span>
  </div>
</footer>

</body>
</html>
```